Dental Bright Keystone Brochure

We need an updated brochure/flyer for our in house dental health membership. We also want to start marketing this to businesses and will need one specifically targeted to businesses as well. Our company colors we need to start branding are red, black and white, however, we don't want the brochure to be too busy with color. We are open to ideas and want something different and eye catching.

Industry/Entity Type

Dental

Font styles to use
Serif

Colors
ec1f27
ffffff
000000

Requirements
Must have
• Brand colors; red, black and white, must have our company logo,
Should not have
• vague and random stock photos

```html
<!DOCTYPE html>
<html lang="en">
<head>
<meta charset="utf-8">
<title>Dental Bright Keystone Brochure</title>
<link rel="stylesheet" href="https://fonts.googleapis.com/css2?family=Lato:wght@400;700;900&family=Oswald:wght@500;600&display=swap">
<style>
:root{
  --red:#ec1f27;
  --ink:#231f20;
  --dark:#2b2a2a;
  --darker:#1c1b1b;
  --grey:#8c8c8c;
  --light:#e9e9e9;
  --white:#ffffff;
  --page:#d9d9d9;
}
*{box-sizing:border-box;margin:0;padding:0}
html,body{width:806px;height:1200px;overflow:hidden}
body{background:var(--page);font-family:"Lato",Arial,sans-serif;color:var(--ink);position:relative}
.sheet{position:absolute;left:33px;width:740px;height:530px;background:var(--white);overflow:hidden;box-shadow:0 4px 12px rgba(0,0,0,.25)}
.sheet--outside{top:40px}
.sheet--inside{top:628px}
.panel{position:absolute;top:0;height:100%;overflow:hidden}
.panel--a{left:0;width:248px}
.panel--b{left:248px;width:244px}
.panel--c{left:492px;width:248px}
.panel--included{top:160px;height:370px;z-index:1}
.dark{background:var(--dark);color:var(--white)}
.photo{position:absolute}
.swoosh{position:absolute;left:0;display:block}
.pill{position:absolute;background:var(--darker);color:var(--red);font-family:"Oswald",sans-serif;font-weight:500;font-size:10.5px;letter-spacing:.4px;padding:3px 10px;border-radius:0 10px 10px 0;text-transform:uppercase}
.body-copy{position:absolute;font-size:9.4px;line-height:12.4px;text-align:justify}
.heading-red{position:absolute;font-family:"Oswald",sans-serif;font-weight:600;color:var(--red);text-transform:uppercase;letter-spacing:.5px}
/* schedule */
.schedule-title{left:0;width:100%;text-align:center;font-size:15px;top:160px}
.schedule-sub{position:absolute;top:186px;width:100%;text-align:center;font-family:"Oswald",sans-serif;font-weight:500;font-size:15px;color:var(--white)}
.schedule-note{position:absolute;top:228px;width:100%;text-align:center;font-size:9.5px;line-height:12px;color:var(--light)}
.benefit-list{position:absolute;top:282px;left:28px;width:190px;list-style:none}
.benefit-list li{display:flex;align-items:baseline;font-size:8.3px;font-weight:700;line-height:14.4px;white-space:nowrap}
.benefit-list .leader{flex:1;border-bottom:1px dotted var(--light);margin:0 2px 2px}
.benefit-list .price{color:var(--red)}
.contact{position:absolute;top:476px;width:100%;text-align:center;font-size:8.5px;font-weight:700;line-height:11px}
.contact svg{vertical-align:-1px;margin-right:3px}
/* cover */
.brand{position:absolute;top:218px;left:40px;display:flex;align-items:center;gap:6px}
.brand-dot{width:16px;height:16px;border-radius:50%;background:var(--red)}
.brand-name{font-size:12px;font-weight:900;color:var(--ink);letter-spacing:.3px}
.brand-tag{position:absolute;top:238px;left:62px;font-size:6px;color:var(--grey)}
.cover-title{position:absolute;top:272px;width:100%;text-align:center;font-family:"Oswald",sans-serif;font-weight:600;font-size:29px;color:var(--red);letter-spacing:.3px;line-height:32px}
.cover-title-2{position:absolute;top:308px;width:100%;text-align:center;font-family:"Oswald",sans-serif;font-weight:500;font-size:28px;color:#555;letter-spacing:1px}
.cover-tag{position:absolute;width:100%;text-align:center}
.cover-tag--1{top:402px;font-size:12.5px;font-weight:700;color:var(--red)}
.cover-tag--2{top:424px;font-size:21px;color:var(--white)}
.cover-tag--3{top:456px;font-size:12px;color:var(--red)}
.phone-pill{position:absolute;top:490px;left:36px;width:176px;height:22px;border-radius:11px;background:var(--white);color:var(--ink);font-weight:700;font-size:13px;letter-spacing:1.5px;text-align:center;line-height:22px}
/* inside */
.check-list{position:absolute;list-style:none;font-size:8.8px;font-weight:700;line-height:15.4px}
.check-list li{position:relative;padding-left:9px}
.check-list li::before{content:"";position:absolute;left:0;top:6px;width:4px;height:4px;border-radius:50%;background:var(--red)}
.check-list .indent{padding-left:9px}
.check-list .indent::before{display:none}
.grey-pill{position:absolute;background:var(--light);color:var(--ink);font-weight:900;font-size:10px;padding:3px 12px;border-radius:0 10px 10px 0}
.small-copy{position:absolute;font-size:8.8px;line-height:11.8px}
.cost-list{position:absolute;list-style:none;font-size:8.8px;font-weight:700;line-height:14.2px}
.cost-list li{position:relative;padding-left:9px}
.cost-list li::before{content:"";position:absolute;left:0;top:6px;width:4px;height:4px;border-radius:50%;background:var(--ink)}
.cost-list .cont{padding-left:9px}
.cost-list .cont::before{display:none}
.red{color:var(--red)}
.rule{position:absolute;height:1px;background:var(--grey)}
</style>
</head>
<body>

<!-- Outside sheet -->
<section class="sheet sheet--outside">

  <div class="panel panel--a">
    <div class="photo" role="img" aria-label="Photo of a patient receiving a teeth whitening treatment" style="left:0;top:0;width:248px;height:205px;background:linear-gradient(135deg,#d9c7b6,#f1ebe4 55%,#b9a89a)"></div>
    <svg class="swoosh" style="top:140px" width="248" height="90" viewBox="0 0 248 90">
      <path d="M0 62 Q120 52 248 4 L248 90 L0 90Z" fill="#fff"/>
      <path d="M0 52 Q120 40 248 -6 L248 6 Q120 54 0 64Z" fill="#ec1f27"/>
      <path d="M0 68 Q120 58 248 10" fill="none" stroke="#8c8c8c" stroke-width="2"/>
    </svg>
    <div class="pill" style="top:245px;left:8px;width:232px">Dental Bright Keystone Premier</div>
    <p class="body-copy" style="top:272px;left:10px;width:228px">includes 100% of your preventive care-cleanings, x-rays, checkup exams—with zero co-pay. It makes it affordable and easy for you to keep up your optimal schedule of preventive visits to maintain your health.<br>Premier membership is a simple agreement between you and Harbor Dental Care; there's no third party involved, no claims to fill out and no worry about whether your claim will be approved.<br>You will know what your benefit and bottom line cost is before you start treatment.<br>Joining is a no-brainer: even if all you need are your regular cleanings, x-rays and exams you will save money. And if you do need more dental work, you will save more, potentially a lot more.</p>
    <svg class="swoosh" style="top:470px" width="248" height="60" viewBox="0 0 248 60">
      <path d="M0 22 Q130 40 248 10" fill="none" stroke="#8c8c8c" stroke-width="2"/>
      <path d="M0 30 Q130 48 248 18 L248 60 L0 60Z" fill="#ec1f27"/>
    </svg>
  </div>

  <div class="panel panel--b dark">
    <svg class="swoosh" style="top:0" width="244" height="160" viewBox="0 0 244 160">
      <path d="M0 0 H108 L122 24 L136 0 H244 V150 Q200 84 122 84 Q44 84 0 150Z" fill="#ec1f27"/>
      <path d="M0 156 Q44 90 122 90 Q200 90 244 156" fill="none" stroke="#fff" stroke-width="1.5"/>
    </svg>
    <svg class="swoosh" style="top:50px;left:64px" width="116" height="116" viewBox="0 0 116 116">
      <circle cx="58" cy="58" r="56" fill="#8c8c8c"/>
      <circle cx="58" cy="58" r="52" fill="#fff"/>
    </svg>
    <div class="photo" role="img" aria-label="Group photo of smiling dental team giving thumbs up" style="left:70px;top:56px;width:104px;height:104px;border-radius:50%;background:radial-gradient(circle at 50% 40%,#f3f3f3,#c8ccd2)"></div>
    <h2 class="heading-red schedule-title">Schedule of Benefits</h2>
    <p class="schedule-sub">(PARTIAL LIST)</p>
    <p class="schedule-note">Benefits are the amounts<br>that will be deducted from the regular fee:</p>
    <ul class="benefit-list">
      <li>Whitening<span class="leader"></span><span class="price">$5130</span></li>
      <li>Composite (white) fillings<span class="leader"></span><span class="price">$40 - $70</span></li>
      <li>Root canals<span class="leader"></span><span class="price">$100</span></li>
      <li>Crowns any type<span class="leader"></span><span class="price">$150</span></li>
      <li>Bridges<span class="leader"></span><span class="price">$5300 - $5600</span></li>
      <li>Porcelain veneers<span class="leader"></span><span class="price">$5170</span></li>
      <li>Complete denture upper or lower<span class="leader"></span><span class="price">$5300</span></li>
      <li>Partial denture upper or lower<span class="leader"></span><span class="price">$5250</span></li>
      <li>Orthodontics<span class="leader"></span><span class="price">$5400 - $5500</span></li>
      <li>Nightguards<span class="leader"></span><span class="price">$50</span></li>
      <li>Implants<span class="leader"></span><span class="price">$5250</span></li>
    </ul>
    <div class="contact">
      <svg width="8" height="8" viewBox="0 0 10 10"><path d="M2 0 L4 2.5 L3 4 Q4.5 6 6 7 L7.5 6 L10 8 L8.5 10 Q3 9.5 0 1.5Z" fill="#ec1f27"/></svg>(555) 014-2290<br>
      <svg width="7" height="7" viewBox="0 0 10 10"><circle cx="5" cy="5" r="4" fill="#ec1f27"/></svg>www.harbordentalcare.example<br>
      18 Elm Row<br>
      <svg width="7" height="9" viewBox="0 0 10 13"><path d="M5 0 A5 5 0 0 1 10 5 Q10 8 5 13 Q0 8 0 5 A5 5 0 0 1 5 0Z" fill="#ec1f27"/><circle cx="5" cy="5" r="2" fill="#2b2a2a"/></svg>Fairview, ME 04000
    </div>
  </div>

  <div class="panel panel--c">
    <div class="photo" role="img" aria-label="Photo of three smiling dentists in white coats" style="left:0;top:0;width:248px;height:190px;background:linear-gradient(135deg,#c9d4df,#eef1f4 50%,#b7c3cf)"></div>
    <svg class="swoosh" style="top:120px" width="248" height="90" viewBox="0 0 248 90">
      <path d="M0 24 Q120 56 248 62 L248 90 L0 90Z" fill="#fff"/>
      <path d="M0 16 Q120 46 248 52 L248 62 Q120 56 0 24Z" fill="#ec1f27"/>
      <path d="M0 30 Q120 62 248 68" fill="none" stroke="#8c8c8c" stroke-width="1.5"/>
    </svg>
    <div class="brand"><span class="brand-dot"></span><span class="brand-name">HARBOR DENTAL CARE</span></div>
    <p class="brand-tag">better smiles, better health... a better life</p>
    <h1 class="cover-title">DENTAL BRIGHT</h1>
    <p class="cover-title-2">KEYSTONE</p>
    <svg class="swoosh" style="top:352px" width="248" height="50" viewBox="0 0 248 50">
      <path d="M0 18 Q130 0 248 16 L248 50 L0 50Z" fill="#2b2a2a"/>
      <path d="M0 12 Q130 -6 248 10" fill="none" stroke="#8c8c8c" stroke-width="4"/>
    </svg>
    <div class="photo dark" style="left:0;top:396px;width:248px;height:134px"></div>
    <p class="cover-tag cover-tag--1">Our exclusive membership plan</p>
    <p class="cover-tag cover-tag--2">giving you benefits</p>
    <p class="cover-tag cover-tag--3">on every dental service we offer!</p>
    <div class="phone-pill">555-014-2290</div>
  </div>
</section>

<!-- Inside sheet -->
<section class="sheet sheet--inside">

  <div class="panel panel--a">
    <svg class="swoosh" style="top:0" width="248" height="150" viewBox="0 0 248 150">
      <path d="M0 0 H248 V70 Q130 110 0 118Z" fill="#2b2a2a"/>
      <path d="M0 112 Q130 106 248 62 L248 76 Q130 120 0 126Z" fill="#ec1f27"/>
      <path d="M0 134 Q130 128 248 84" fill="none" stroke="#8c8c8c" stroke-width="1.5"/>
    </svg>
    <svg class="swoosh" style="top:18px;left:60px" width="124" height="124" viewBox="0 0 124 124">
      <circle cx="62" cy="62" r="61" fill="#ec1f27"/>
      <circle cx="62" cy="62" r="56" fill="#fff"/>
    </svg>
    <div class="photo" role="img" aria-label="Photo of a patient during a dental examination" style="left:66px;top:24px;width:112px;height:112px;border-radius:50%;background:radial-gradient(circle at 50% 45%,#e6eef3,#a9bccb)"></div>
    <div class="pill" style="top:172px;left:0;padding-left:8px">Advantages</div>
    <ul class="check-list" style="top:204px;left:10px;width:232px">
      <li>It's not insurance; no third party; no red tape</li>
      <li>Affordable predictable cost,</li>
      <li class="indent">automatic payments</li>
      <li>No waiting period</li>
      <li>No deductible ever</li>
      <li>No annual maximum</li>
      <li>No claim forms, no claims to be denied, no</li>
      <li class="indent">stalled payments</li>
      <li>No pre-authorizations</li>
      <li>Choice of coverage to fit your needs; tailor</li>
      <li class="indent">your plan to fit you</li>
      <li>Know your exact coverage before treatment</li>
      <li>You choose the treatment;</li>
      <li class="indent">no third party interference</li>
      <li>Includes benefits for cosmetic dentistry and</li>
      <li class="indent">orthodontics, and other services usually not</li>
      <li class="indent">included in dental insurance-plans</li>
    </ul>
  </div>

  <div class="photo" role="img" aria-label="Photo of five smiling dental professionals in a row" style="left:248px;top:0;width:492px;height:170px;background:linear-gradient(90deg,#e4e4e4,#f7f7f7 50%,#dcdcdc)"></div>
  <svg class="swoosh" style="top:100px;left:248px" width="492" height="90" viewBox="0 0 492 90">
    <path d="M0 40 Q250 48 492 84 L492 90 L0 90Z" fill="#2b2a2a"/>
    <path d="M244 54 Q370 64 492 84 L492 90 L244 90Z" fill="#fff"/>
    <path d="M0 22 Q250 30 492 66" fill="none" stroke="#8c8c8c" stroke-width="1.5"/>
    <path d="M0 28 Q250 36 492 72 L492 84 Q250 48 0 40Z" fill="#ec1f27"/>
  </svg>

  <div class="panel panel--b panel--included dark">
    <div class="heading-red" style="top:10px;left:10px;font-size:14px">What's Included?</div>
    <div class="grey-pill" style="top:38px;left:0;width:200px">PREVENTIVE SERVICES AT 100%</div>
    <ul class="check-list" style="top:70px;left:14px;width:224px;font-size:8.6px;line-height:13.5px">
      <li>Your regular twice-a-year cleanings</li>
      <li class="indent">or 4-times-a-year periodontal maintenance</li>
      <li>Dental exam by the doctor each year</li>
      <li>Necessary x-rays</li>
      <li>Fluoride treatments</li>
    </ul>
    <div class="grey-pill" style="top:162px;left:0;width:58px">PLUS</div>
    <ul class="check-list" style="top:192px;left:14px;width:224px;font-size:8.6px;line-height:12px">
      <li>Teeth whitening - 50% off</li>
      <li>Benefits for fillings, crowns, bridges</li>
      <li class="indent">orthodontics, veneers and implants</li>
    </ul>
    <div class="heading-red" style="top:242px;left:10px;font-size:14px">How do I qualify?</div>
    <p class="small-copy" style="top:268px;left:10px;width:226px;color:var(--light)">You must be a patient of record of Harbor Dental Care in good standing (you may sign up after your initial exam, if you are a new patient)</p>
  </div>

  <div class="panel panel--c" style="top:170px;height:360px">
    <div class="heading-red" style="top:24px;left:0;font-size:14px;padding-left:2px">What's the catch?</div>
    <div class="rule" style="top:46px;left:0;width:150px"></div>
    <p class="small-copy" style="top:58px;left:4px;width:236px">No catch, no hidden costs. This plan reflects the fact that those who meet the conditions outlined above reduce our costs. These savings are passed back to you.</p>
    <div class="heading-red" style="top:122px;left:0;font-size:14px;padding-left:2px">What's the cost?</div>
    <div class="rule" style="top:144px;left:0;width:150px"></div>
    <ul class="cost-list" style="top:152px;left:4px;width:240px">
      <li>Set-up Fee (applies to all plans)</li>
      <li class="cont"><span class="red">$45</span> per person, <span class="red">$90</span> maximum per family</li>
      <li>Basic preventive plan</li>
      <li class="cont">two preventive visits per year restorative</li>
      <li class="cont">benefits Individual <span class="red">$27</span> per month</li>
      <li>Periodontal maintenance plan</li>
      <li class="cont">four maintenance visits/yr.</li>
      <li class="cont">restorative benefits Individual <span class="red">$552</span> per month</li>
      <li>Children* <span class="red">(under 18)</span>, basic preventive plan</li>
      <li class="cont"><span class="red">$20</span> per month</li>
    </ul>
  </div>

  <svg class="swoosh" style="top:474px;z-index:2" width="740" height="56" viewBox="0 0 740 56">
    <path d="M0 22 Q380 52 740 8" fill="none" stroke="#8c8c8c" stroke-width="2"/>
    <path d="M0 30 Q380 60 740 16 L740 56 L0 56Z" fill="#ec1f27"/>
  </svg>
</section>

</body>
</html>
```